customer services company for the travel industry needs a flyer designed

we need a flyer for our London based company. We are an outsource service to the travel industry so our client companies receive a complaint from their customer about their holiday or travel arrangements and they pass it to us to handle. We take the stress and strain away from them that complaints present! check out our website www.fernmoorassist.co.uk - blue features as our corporate colors. The business is 26 years old so well established in the industry. The reverse of the flyer will be printed with endorsements from current company clients. I would like something light hearted projecting the relief of pressure we can provide whilst also suggesting complaints and complainants will be in professional safe capable hands

Industry/Entity Type

Travel

```html
<!DOCTYPE html>
<html lang="en">
<head>
<meta charset="utf-8">
<title>Fernmoor Assist – Flyer</title>
<link rel="stylesheet" href="https://fonts.googleapis.com/css2?family=Arimo:ital,wght@0,400;1,400;1,700&family=Pathway+Gothic+One&family=Tinos&display=swap">
<style>
  :root {
    --blue-deep: #0f63a6;
    --blue-sky: #27a9e1;
    --blue-pale: #8ecae6;
    --grey-band: #a9adb1;
    --grey-text: #6d6f72;
    --ink-teal: #2a6f98;
    --logo-blue: #2f7fb9;
    --white: #ffffff;
  }
  html, body {
    margin: 0;
    width: 1200px;
    height: 1000px;
    overflow: hidden;
    background: #ffffff;
  }
  .flyer {
    position: relative;
    width: 1200px;
    height: 1000px;
  }
  .sheet {
    position: absolute;
    left: 12px; top: 0;
    width: 1108px; height: 996px;
    background: var(--white);
    border-left: 2px solid #222;
    border-top: 2px solid #222;
    box-shadow: 8px 6px 10px rgba(0,0,0,0.45);
  }
  .shapes { position: absolute; left: 0; top: 0; }
  .brand {
    position: absolute; left: 76px; top: 14px;
  }
  .brand-name {
    font-family: "Arimo", sans-serif;
    font-size: 34px;
    color: var(--logo-blue);
    line-height: 1;
    margin: 8px 0 4px;
  }
  .brand-tagline {
    font-family: "Arimo", sans-serif;
    font-style: italic;
    font-size: 11px;
    color: var(--grey-text);
    padding-left: 88px;
  }
  .headline {
    position: absolute; left: 34px; top: 208px;
    font-family: "Pathway Gothic One", sans-serif;
    font-style: italic;
    font-size: 48px;
    color: var(--white);
    margin: 0;
    line-height: 1.2;
  }
  .intro {
    position: absolute; left: 75px; top: 543px;
    font-family: "Tinos", serif;
    font-size: 28px;
    line-height: 37px;
    color: var(--ink-teal);
    margin: 0;
  }
  .provide-label {
    position: absolute; left: 140px; top: 634px;
    font-family: "Tinos", serif;
    font-size: 27px;
    color: var(--ink-teal);
    margin: 0;
  }
  .services {
    position: absolute; left: 76px; top: 676px;
    list-style: none; margin: 0; padding: 0;
  }
  .services li {
    display: flex; align-items: center;
    height: 45px;
    font-family: "Arimo", sans-serif;
    font-style: italic;
    font-size: 35px;
    color: var(--ink-teal);
    white-space: nowrap;
  }
  .services svg { margin-right: 5px; flex: none; }
  .traveller-photo {
    position: absolute; left: 70px; top: 772px;
    width: 192px; height: 166px;
    background: linear-gradient(135deg, #cfe7ee 0%, #8fb7c9 50%, #3c5f86 100%);
  }
  .call-to-action {
    position: absolute; left: 270px; top: 790px;
    font-family: "Tinos", serif;
    font-size: 35.5px;
    line-height: 43px;
    color: var(--ink-teal);
    margin: 0;
  }
  .contact {
    position: absolute; left: 770px; top: 786px;
    font-family: "Arimo", sans-serif;
    font-style: italic; font-weight: 700;
    font-size: 16px; line-height: 21px;
    color: var(--white);
    margin: 0;
  }
  .contact .indent { padding-left: 70px; display: block; }
  .contact .gap { display: block; height: 21px; }
  .website {
    position: absolute; left: 243px; top: 952px;
    font-family: "Arimo", sans-serif;
    font-style: italic; font-weight: 700;
    font-size: 28px;
    color: var(--white);
    margin: 0; line-height: 1.2;
  }
</style>
</head>
<body>
<main class="flyer">
  <div class="sheet"></div>

  <svg class="shapes" width="1200" height="1000" viewBox="0 0 1200 1000">
    <defs>
      <linearGradient id="sky" x1="0" y1="0" x2="0" y2="1">
        <stop offset="0" stop-color="#8fa9c2"/>
        <stop offset="0.35" stop-color="#b9cadb"/>
        <stop offset="0.7" stop-color="#e4ebf2"/>
        <stop offset="1" stop-color="#f4f6f9"/>
      </linearGradient>
      <radialGradient id="haze" cx="0.55" cy="0.45" r="0.5">
        <stop offset="0" stop-color="#ffffff" stop-opacity="0.55"/>
        <stop offset="1" stop-color="#ffffff" stop-opacity="0"/>
      </radialGradient>
    </defs>
    <g aria-hidden="true">
      <!-- top arrow band -->
      <polygon points="14,82 150,82 183,110 150,138 14,138" fill="var(--blue-deep)"/>
      <polygon points="325,82 778,82 812,110 778,138 325,138 355,110" fill="var(--blue-sky)"/>
      <polygon points="820,82 1120,82 1120,138 812,138 840,110" fill="var(--grey-band)"/>
      <!-- hero frame -->
      <rect x="860" y="170" width="260" height="352" fill="var(--blue-sky)"/>
      <polygon points="860,170 900,170 1048,346 900,522 860,522 1008,346" fill="var(--white)"/>
    </g>
    <!-- hero photograph area -->
    <g role="img" aria-label="Passenger jet flying above white clouds in a pale blue sky">
      <polygon points="14,170 860,170 1008,346 860,522 14,522" fill="url(#sky)"/>
      <polygon points="14,170 860,170 1008,346 860,522 14,522" fill="url(#haze)"/>
    </g>
    <g aria-hidden="true">
      <!-- headline banner -->
      <polygon points="14,192 470,192 510,237 470,283 14,283" fill="var(--grey-band)" opacity="0.92"/>
      <!-- bottom band -->
      <polygon points="14,945 150,945 178,966 150,988 14,988" fill="var(--blue-deep)"/>
      <polygon points="215,945 1118,945 1118,988 215,988 240,966" fill="var(--blue-sky)"/>
      <!-- address panel -->
      <path d="M762,775 H1115 V905 Q1090,952 985,962 Q870,964 762,942 Z" fill="var(--blue-pale)"/>
    </g>
  </svg>

  <h1 class="headline">Make your life a little easier</h1>

  <header class="brand">
    <div class="brand-name">Fernmoor Assist</div>
    <div class="brand-tagline">Customer Service &amp; Training Specialists</div>
  </header>

  <p class="intro">Our professional, experienced team manage customer service issues and<br>complaints for travel companies serving the UK and Ireland markets .</p>
  <p class="provide-label">We provide:</p>

  <ul class="services">
    <li>
      <svg width="48" height="28" viewBox="0 0 48 28" aria-hidden="true"><ellipse cx="24" cy="14" rx="23" ry="12" fill="#1b5e9e"/><ellipse cx="24" cy="12" rx="19" ry="8" fill="#e8f3fb"/><path d="M15,11 L22,18 L34,6" fill="none" stroke="#1b5e9e" stroke-width="4" stroke-linecap="round" stroke-linejoin="round"/></svg>
      Complaints management services
    </li>
    <li>
      <svg width="48" height="28" viewBox="0 0 48 28" aria-hidden="true"><ellipse cx="24" cy="14" rx="23" ry="12" fill="#1b5e9e"/><ellipse cx="24" cy="12" rx="19" ry="8" fill="#e8f3fb"/><path d="M15,11 L22,18 L34,6" fill="none" stroke="#1b5e9e" stroke-width="4" stroke-linecap="round" stroke-linejoin="round"/></svg>
      Customer service training courses for the travel trade industry
    </li>
  </ul>

  <div class="traveller-photo" role="img" aria-label="Traveller pulling a blue suitcase along an airport moving walkway"></div>
  <p class="call-to-action">Contact us today,<br>save your business time,<br>money and stress</p>

  <address class="contact">
    Address: Unit 27 Halden Yard
    <span class="indent">48-52 Ashcombe Road</span>
    <span class="indent">London</span>
    <span class="indent">N7 2QT</span>
    <span class="gap"></span>
    Tel: +44 20 7000 4821<br>
    Email: custserv@fernmoorassist.co.uk
  </address>

  <p class="website">www.fernmoorassist.co.uk</p>
</main>
</body>
</html>
```